Business Association Needs Anti-Litter Poster

We are a business association that works to keep our business district clean and safe. We work very hard to keep our streets and parks clean. We are located in a very densely populated part of the city with residents from many parts of the world. We would like a unique poster that that appeals to a multicultural community and reminds residents not to litter. Our community is called City Heights and is located within San Diego, California, USA. Our organizational web site is www.ferndalewalkba.org

Reason: I extended the deadline in order to provided enough time to get feedback from my committee on which design they like best for the campaign.

```html
<!DOCTYPE html>
<html lang="en">
<head>
<meta charset="utf-8">
<title>Do Not Litter – Ferndale Walk Business Association</title>
<link href="https://fonts.googleapis.com/css2?family=Anton&family=Cinzel:wght@700&family=Oswald:wght@500&display=swap" rel="stylesheet">
<style>
  :root {
    --paper-light: #fafafa;
    --paper-dark: #e9e9e9;
    --ink: #111111;
    --orange: #e8821e;
    --red: #d0242c;
    --brown: #7a5417;
    --footer-bg: #0b0b0b;
    --footer-text: #f4e27a;
    --sky: #c9dff0;
    --street: #8f8f8c;
    --greenery: #7d8f6a;
  }
  html, body { margin: 0; padding: 0; overflow: hidden; }
  body { width: 954px; height: 1200px; background: #ffffff; }

  .poster {
    position: relative;
    width: 954px;
    height: 1200px;
    overflow: hidden;
    background: radial-gradient(ellipse at 40% 35%, var(--paper-light) 0%, #f2f2f2 60%, var(--paper-dark) 100%);
  }

  .brand {
    position: absolute;
    top: 38px;
    left: 0;
    width: 954px;
    text-align: center;
  }
  .brand-mark {
    display: block;
    width: 104px;
    height: 104px;
    margin: 0 auto 22px;
    border-radius: 50%;
    background: var(--orange);
  }
  .brand-name {
    margin: 0;
    font-family: "Cinzel", serif;
    font-weight: 700;
    font-size: 28px;
    line-height: 1.15;
    color: var(--ink);
  }

  .gallery {
    position: absolute;
    top: 267px;
    left: 35px;
    width: 872px;
    height: 295px;
    box-shadow: 0 4px 8px rgba(0,0,0,0.35);
  }
  .gallery-main {
    position: absolute;
    top: 0; left: 0;
    width: 872px; height: 192px;
    background: linear-gradient(180deg, var(--sky) 0%, #d9e3e6 45%, #9aa27f 62%, var(--street) 100%);
  }
  .gallery-row {
    position: absolute;
    top: 195px; left: 0;
    width: 872px; height: 100px;
    display: flex;
    gap: 3px;
  }
  .gallery-thumb { flex: 1; height: 100px; }
  .thumb-a { background: linear-gradient(180deg, #9aa0a4, #6f7375); }
  .thumb-b { background: linear-gradient(180deg, #b7c3b0, var(--greenery)); }
  .thumb-c { background: linear-gradient(180deg, #a9b7a0, #6e7b5c); }
  .thumb-d { background: linear-gradient(180deg, #b8b4ae, #6c6a66); }
  .thumb-e { background: linear-gradient(180deg, #c9c3cc, #8e8790); }
  .thumb-f { background: linear-gradient(180deg, #a4b39a, #5f6f50); }

  .tagline {
    position: absolute;
    top: 585px;
    left: 0;
    width: 954px;
    margin: 0;
    text-align: center;
    font-family: "Cinzel", serif;
    font-weight: 700;
    font-size: 31px;
    line-height: 38px;
    letter-spacing: 2.5px;
    text-transform: uppercase;
    color: var(--ink);
    white-space: nowrap;
  }

  .slogan { position: absolute; inset: 0; pointer-events: none; }
  .letter {
    position: absolute;
    font-family: "Anton", sans-serif;
    line-height: 1;
    transform-origin: center;
  }
  .word-do  { color: var(--orange); font-size: 190px; }
  .word-not { color: var(--red); font-size: 190px; }
  .word-litter { color: var(--brown); font-size: 215px; }

  .footer {
    position: absolute;
    left: 0;
    bottom: 0;
    width: 954px;
    height: 48px;
    background: var(--footer-bg);
    display: flex;
    align-items: center;
    justify-content: center;
    font-family: "Oswald", sans-serif;
    font-weight: 500;
    font-size: 15px;
    color: var(--footer-text);
    letter-spacing: 0.2px;
  }
  .footer span { margin: 0 6px; }
</style>
</head>
<body>
<main class="poster">
  <header class="brand">
    <span class="brand-mark"></span>
    <p class="brand-name">Ferndale Walk<br>Business Association</p>
  </header>

  <section class="gallery">
    <div class="gallery-main" role="img" aria-label="Wide street view of the business district with traffic lights, palm trees and shops"></div>
    <div class="gallery-row">
      <div class="gallery-thumb thumb-a" role="img" aria-label="Crew member pressure-washing the sidewalk"></div>
      <div class="gallery-thumb thumb-b" role="img" aria-label="Worker with a leaf blower clearing a walkway"></div>
      <div class="gallery-thumb thumb-c" role="img" aria-label="Volunteer clearing weeds along a fence"></div>
      <div class="gallery-thumb thumb-d" role="img" aria-label="Officers talking with a community member"></div>
      <div class="gallery-thumb thumb-e" role="img" aria-label="Worker cleaning beside a bus shelter"></div>
      <div class="gallery-thumb thumb-f" role="img" aria-label="Crew bagging litter along a planted strip"></div>
    </div>
  </section>

  <h1 class="tagline">Please Lets Keep San Diego’s<br>International Marketplace Clean</h1>

  <div class="slogan" aria-label="Do not litter">
    <span class="letter word-do" style="left:232px; top:664px; transform:rotate(-4deg);">D</span>
    <span class="letter word-do" style="left:334px; top:716px; transform:rotate(3deg);">O</span>
    <span class="letter word-not" style="left:470px; top:678px; transform:rotate(-6deg);">N</span>
    <span class="letter word-not" style="left:578px; top:742px; transform:rotate(5deg);">O</span>
    <span class="letter word-not" style="left:672px; top:690px; transform:rotate(8deg);">T</span>

    <span class="letter word-litter" style="left:150px; top:930px; transform:rotate(8deg);">L</span>
    <span class="letter word-litter" style="left:240px; top:920px; transform:rotate(-10deg);">I</span>
    <span class="letter word-litter" style="left:305px; top:900px; transform:rotate(-4deg);">T</span>
    <span class="letter word-litter" style="left:420px; top:912px; transform:rotate(3deg);">T</span>
    <span class="letter word-litter" style="left:535px; top:912px; transform:rotate(-3deg);">E</span>
    <span class="letter word-litter" style="left:660px; top:922px; transform:rotate(-8deg);">R</span>
  </div>

  <footer class="footer">
    <span>Ferndale Walk Business Association</span>|
    <span>2180 Meridian Avenue, Suite 310</span>|
    <span>San Diego, CA 92199</span>|
    <span>555-014-2290</span>
  </footer>
</main>
</body>
</html>
```